Modern Billboard Ad for Criminal Defense Firm

10.5 x 36 We're looking for something to set us apart from the local competition. Looking for sleek and modern. We're a mid-sized firm in a small market city. We want to give the artist room to be creative on this one.
Thanks

Target Market(s)

Adult clients who have been charged with a crime/DWI

Industry/Entity Type

legal

Font styles to use
Serif
Sans Serif

Requirements
Must have
• Needs to have the firm name in large lettering. Law Offices of Marcus T Whitfield. “PLLC” does not have to be included. Phone number of (555) 384-1927 should be included but not the main focus.
Nice to have
• A call to action or something similar. “Don’t go it alone, call today.”, “ Arrested?”

```html
<!DOCTYPE html>
<html lang="en">
<head>
<meta charset="utf-8">
<title>Billboard – Law Offices of Marcus T Whitfield</title>
<link href="https://fonts.googleapis.com/css2?family=Michroma&family=Montserrat:ital,wght@0,600;0,700;1,600&family=Oswald:wght@500;600&display=swap" rel="stylesheet">
<style>
  :root {
    --backdrop: #5b5b5b;
    --charcoal: #231f20;
    --ink: #363636;
    --navy-deep: #0b2240;
    --navy: #2f3b7c;
    --navy-line: #2a3470;
    --gold: #f6a21c;
    --gold-line: #c9952c;
    --white: #ffffff;
  }
  html, body {
    margin: 0;
    width: 1200px;
    height: 956px;
    overflow: hidden;
    background: var(--backdrop);
  }
  .billboard {
    position: absolute;
    left: 20px;
    top: 308px;
    width: 1160px;
    height: 339px;
    box-shadow: 0 18px 30px rgba(0,0,0,.35);
  }
  .headline-small { font-family: "Michroma", sans-serif; font-size: 50px; fill: var(--ink); stroke: var(--ink); stroke-width: 1.6; }
  .headline-large { font-family: "Montserrat", sans-serif; font-weight: 700; font-size: 112px; fill: var(--ink); }
  .tagline { font-family: "Montserrat", sans-serif; font-style: italic; font-weight: 600; font-size: 40px; fill: var(--navy-line); }
  .phone-number { font-family: "Montserrat", sans-serif; font-weight: 700; font-size: 90px; fill: var(--white); }
  .firm-prefix { font-family: "Oswald", sans-serif; font-weight: 500; font-size: 28px; fill: var(--charcoal); }
  .firm-name { font-family: "Oswald", sans-serif; font-weight: 600; font-size: 66px; fill: var(--charcoal); }
</style>
</head>
<body>
<svg class="billboard" viewBox="0 0 1985 580" xmlns="http://www.w3.org/2000/svg">
  <defs>
    <linearGradient id="portraitTone" x1="0" y1="0" x2="0" y2="1">
      <stop offset="0" stop-color="#231f20"/>
      <stop offset="0.45" stop-color="#3a3839"/>
      <stop offset="1" stop-color="#8a8a8a"/>
    </linearGradient>
  </defs>

  <!-- blue lower band -->
  <polygon class="lower-band" points="695,290 1985,290 1985,580 640,580" fill="var(--navy)"/>
  <!-- white upper panel -->
  <polygon class="upper-panel" points="745,0 1985,0 1985,290 695,290" fill="var(--white)"/>
  <!-- navy diagonal stripe -->
  <polygon class="accent-stripe" points="663,0 745,0 645,580 560,580" fill="var(--navy-deep)"/>
  <!-- attorney portrait area -->
  <polygon class="portrait" role="img" aria-label="Black and white portrait photo of the two firm attorneys in suits"
           points="0,0 663,0 600,365 665,580 0,580" fill="url(#portraitTone)"/>
  <line class="gold-rule" x1="663" y1="0" x2="600" y2="365" stroke="var(--gold-line)" stroke-width="4"/>

  <!-- firm name bar -->
  <polygon class="firm-bar" points="0,432 700,432 684,562 0,562" fill="var(--gold)"/>
  <text class="firm-prefix" x="340" y="470" text-anchor="middle" textLength="300" lengthAdjust="spacing">LAW OFFICES OF</text>
  <text class="firm-name" x="340" y="543" text-anchor="middle" textLength="610" lengthAdjust="spacing">MARCUS T WHITFIELD</text>

  <!-- headlines -->
  <text class="headline-small" x="1328" y="108" text-anchor="middle" textLength="855" lengthAdjust="spacing">DON’T GO IT ALONE</text>
  <text class="headline-large" x="1328" y="214" text-anchor="middle" textLength="855" lengthAdjust="spacingAndGlyphs">CALL TODAY!</text>

  <!-- tagline box -->
  <rect class="tagline-box" x="914" y="256" width="840" height="66" fill="var(--white)" stroke="var(--navy-line)" stroke-width="4"/>
  <text class="tagline" x="1334" y="303" text-anchor="middle" textLength="540" lengthAdjust="spacing">“ARRESTED?”</text>

  <!-- phone icon -->
  <g class="phone-icon" fill="none" stroke="var(--gold)" stroke-width="6" stroke-linecap="round" stroke-linejoin="round">
    <path d="M858,424 l18,-8 l16,30 l-12,10 q10,26 34,40 l12,-10 l28,18 l-6,18 q-6,10 -18,8 q-40,-10 -68,-50 q-18,-28 -12,-46 q2,-8 8,-10 z"/>
    <path d="M902,432 q20,2 26,24"/>
    <path d="M906,414 q34,4 42,40"/>
    <path d="M910,396 q48,6 58,56"/>
  </g>

  <!-- phone number -->
  <text class="phone-number" x="995" y="482" textLength="760" lengthAdjust="spacingAndGlyphs">(555) 384-1927</text>
</svg>
</body>
</html>
```